100% No Money Down

Flyer Design

Used for IG & FB (Social Media) Post. So avoid 8 1/2 x 11.

Target Market(s)

Real Estate Investors

Industry/Entity Type

Mortgage Brokerage

Requirements
Must have
• (LARGE BOLD FONT)
• 100% Investor Financing
• Fix & Flip Joint Ventures
• * Closing Costs Financed
• * 2-3 Week Close
• * No Score Minimum
• * No Reserve Requirement
• Contact: Marcus Delwyn
• Bluegate Lending Partners, Inc.
• NMLS #58307 / #916482
• Direct (240) 555-0193
• Email mdelwyn@bluegatelendpro.com

```html
<!DOCTYPE html>
<html lang="en">
<head>
<meta charset="utf-8">
<title>100% No Money Down – Investor Financing Flyer</title>
<link href="https://fonts.googleapis.com/css2?family=Montserrat:wght@700;800;900&family=Cinzel:wght@700;800&display=swap" rel="stylesheet">
<style>
  :root{
    --page:#cfcfcf;
    --gold:#d4c483;
    --gold-deep:#b9a45a;
    --ink-dark:#2a2a2c;
    --ink-mid:#333335;
    --white:#ffffff;
  }
  *{margin:0;padding:0;box-sizing:border-box}
  html,body{width:1200px;height:1200px;overflow:hidden;background:var(--page)}
  .canvas{position:relative;width:1200px;height:1200px;overflow:hidden}
  .flyer{
    position:absolute;left:193px;top:18px;width:838px;height:1193px;
    transform:scale(0.97);transform-origin:top left;
    box-shadow:0 10px 24px rgba(0,0,0,.35);overflow:hidden;background:var(--ink-dark);
  }
  .flyer-art{position:absolute;inset:0}
  .brand{
    position:absolute;left:92px;top:118px;width:290px;
    display:flex;align-items:center;gap:12px;
    font-family:"Montserrat",sans-serif;font-weight:800;font-size:19px;line-height:1.15;color:var(--gold-deep);
  }
  .brand-dot{width:34px;height:34px;border-radius:50%;background:var(--gold-deep);flex:none}
  .headline{
    position:absolute;left:70px;top:262px;
    font-family:"Montserrat",sans-serif;font-weight:900;font-size:46px;line-height:47px;
    color:var(--gold);text-transform:uppercase;letter-spacing:-.5px;
    text-shadow:1px 1px 0 #8f8150;
  }
  .sc{font-family:"Cinzel",serif;font-weight:700;color:var(--white)}
  .gold-head{font-family:"Montserrat",sans-serif;font-weight:800;color:var(--gold);text-transform:uppercase}
  .contact{position:absolute;left:33px;top:740px;width:330px}
  .contact .gold-head{font-size:24px;line-height:28px}
  .contact-list{list-style:none;margin-top:18px;font-size:17px;line-height:26.5px}
  .contact-list .indent{padding-left:10px}
  .label{font-size:25px;line-height:28px;margin-top:18px}
  .value{font-family:"Montserrat",sans-serif;font-weight:700;font-size:15px;color:var(--white);margin-top:2px;letter-spacing:.3px}
  .phones{display:flex;align-items:center;gap:16px;margin-top:24px}
  .phones .lines{font-family:"Montserrat",sans-serif;font-weight:700;font-size:17px;line-height:27px;color:var(--white)}
  .offer{position:absolute;left:390px;top:766px;width:430px}
  .offer .gold-head{font-size:24px;line-height:32px}
  .perks{list-style:none;margin-top:34px;font-size:16.5px;line-height:23px}
  .terms{list-style:none;margin-top:30px;font-size:16.5px;line-height:25px}
  .terms .sc{color:var(--gold)}
</style>
</head>
<body>
<div class="canvas">
  <div class="flyer">
    <svg class="flyer-art" viewBox="0 0 838 1193" width="838" height="1193">
      <defs>
        <linearGradient id="heroBase" x1="0" y1="0" x2="1" y2="1">
          <stop offset="0" stop-color="#e6eae8"/>
          <stop offset=".5" stop-color="#c9cecb"/>
          <stop offset="1" stop-color="#9a9d9b"/>
        </linearGradient>
        <radialGradient id="heroSuit" cx="560" cy="430" r="330" gradientUnits="userSpaceOnUse">
          <stop offset="0" stop-color="#6e6f72"/>
          <stop offset=".6" stop-color="#8a8c8e" stop-opacity=".7"/>
          <stop offset="1" stop-color="#8a8c8e" stop-opacity="0"/>
        </radialGradient>
        <radialGradient id="heroWarm" cx="610" cy="220" r="150" gradientUnits="userSpaceOnUse">
          <stop offset="0" stop-color="#5a3d2c"/>
          <stop offset=".55" stop-color="#6b4b3a" stop-opacity=".6"/>
          <stop offset="1" stop-color="#6b4b3a" stop-opacity="0"/>
        </radialGradient>
        <radialGradient id="heroGreen" cx="760" cy="90" r="180" gradientUnits="userSpaceOnUse">
          <stop offset="0" stop-color="#9fb3a5" stop-opacity=".8"/>
          <stop offset="1" stop-color="#9fb3a5" stop-opacity="0"/>
        </radialGradient>
        <linearGradient id="panelFade" x1="0" y1="0" x2="0" y2="1">
          <stop offset="0" stop-color="#ffffff" stop-opacity=".85"/>
          <stop offset=".75" stop-color="#ffffff" stop-opacity=".6"/>
          <stop offset="1" stop-color="#ffffff" stop-opacity=".2"/>
        </linearGradient>

        <clipPath id="clipOffice"><circle cx="162" cy="573" r="126"/></clipPath>
        <clipPath id="clipSite"><circle cx="425" cy="521" r="130"/></clipPath>
        <clipPath id="clipKitchen"><circle cx="685" cy="493" r="135"/></clipPath>

        <linearGradient id="officeBase" x1="0" y1="0" x2="1" y2="0">
          <stop offset="0" stop-color="#f4efe6"/><stop offset=".6" stop-color="#e7dccb"/><stop offset="1" stop-color="#f6f2ea"/>
        </linearGradient>
        <radialGradient id="officeSweater" cx="190" cy="600" r="110" gradientUnits="userSpaceOnUse">
          <stop offset="0" stop-color="#34384a"/><stop offset=".7" stop-color="#474b5c" stop-opacity=".8"/><stop offset="1" stop-color="#474b5c" stop-opacity="0"/>
        </radialGradient>
        <linearGradient id="officeDesk" x1="0" y1="0" x2="0" y2="1">
          <stop offset="0" stop-color="#c98f58" stop-opacity="0"/><stop offset=".75" stop-color="#cf9a63" stop-opacity=".85"/><stop offset="1" stop-color="#b57b45"/>
        </linearGradient>

        <linearGradient id="siteBase" x1="0" y1="0" x2="0" y2="1">
          <stop offset="0" stop-color="#d7d4cc"/><stop offset=".45" stop-color="#b9aa92"/><stop offset="1" stop-color="#5d3f4a"/>
        </linearGradient>
        <radialGradient id="siteHat" cx="430" cy="440" r="70" gradientUnits="userSpaceOnUse">
          <stop offset="0" stop-color="#f2c22c"/><stop offset=".6" stop-color="#e7b93a" stop-opacity=".55"/><stop offset="1" stop-color="#e7b93a" stop-opacity="0"/>
        </radialGradient>
        <radialGradient id="siteShirt" cx="430" cy="640" r="130" gradientUnits="userSpaceOnUse">
          <stop offset="0" stop-color="#3a3b6a"/><stop offset=".55" stop-color="#7a2f3c" stop-opacity=".75"/><stop offset="1" stop-color="#7a2f3c" stop-opacity="0"/>
        </radialGradient>

        <linearGradient id="kitchenBase" x1="0" y1="0" x2="1" y2="1">
          <stop offset="0" stop-color="#fafaf8"/><stop offset=".5" stop-color="#e3e2de"/><stop offset="1" stop-color="#c8c6bf"/>
        </linearGradient>
        <radialGradient id="kitchenCash" cx="720" cy="520" r="95" gradientUnits="userSpaceOnUse">
          <stop offset="0" stop-color="#8f8c6a"/><stop offset=".55" stop-color="#a9a585" stop-opacity=".7"/><stop offset="1" stop-color="#a9a585" stop-opacity="0"/>
        </radialGradient>
        <radialGradient id="kitchenLamp" cx="630" cy="430" r="70" gradientUnits="userSpaceOnUse">
          <stop offset="0" stop-color="#d8c9a3" stop-opacity=".8"/><stop offset="1" stop-color="#d8c9a3" stop-opacity="0"/>
        </radialGradient>
      </defs>

      <g role="img" aria-label="Photo of a smiling investor in a grey suit with banknotes falling around him">
        <rect x="0" y="0" width="838" height="700" fill="url(#heroBase)"/>
        <rect x="0" y="0" width="838" height="700" fill="url(#heroGreen)"/>
        <rect x="0" y="0" width="838" height="700" fill="url(#heroSuit)"/>
        <rect x="0" y="0" width="838" height="700" fill="url(#heroWarm)"/>
      </g>
      <rect x="32" y="0" width="370" height="600" fill="url(#panelFade)"/>

      <polygon points="0,653 838,473 838,1193 0,1193" fill="var(--ink-mid)"/>
      <polygon points="0,653 357,576 357,1193 0,1193" fill="var(--ink-dark)"/>

      <g role="img" aria-label="Photo of an older man working on paperwork with a calculator">
        <g clip-path="url(#clipOffice)">
          <rect x="30" y="440" width="270" height="270" fill="url(#officeBase)"/>
          <rect x="30" y="440" width="270" height="270" fill="url(#officeDesk)"/>
          <rect x="30" y="440" width="270" height="270" fill="url(#officeSweater)"/>
        </g>
        <circle cx="162" cy="573" r="126" fill="none" stroke="var(--white)" stroke-width="9"/>
      </g>
      <g role="img" aria-label="Photo of a smiling contractor in a yellow hard hat carrying lumber">
        <g clip-path="url(#clipSite)">
          <rect x="290" y="385" width="275" height="275" fill="url(#siteBase)"/>
          <rect x="290" y="385" width="275" height="275" fill="url(#siteShirt)"/>
          <rect x="290" y="385" width="275" height="275" fill="url(#siteHat)"/>
        </g>
        <circle cx="425" cy="521" r="130" fill="none" stroke="var(--white)" stroke-width="9"/>
      </g>
      <g role="img" aria-label="Photo of a renovated kitchen with a hand holding a stack of cash">
        <g clip-path="url(#clipKitchen)">
          <rect x="545" y="355" width="280" height="280" fill="url(#kitchenBase)"/>
          <rect x="545" y="355" width="280" height="280" fill="url(#kitchenLamp)"/>
          <rect x="545" y="355" width="280" height="280" fill="url(#kitchenCash)"/>
        </g>
        <circle cx="685" cy="493" r="135" fill="none" stroke="var(--white)" stroke-width="9"/>
      </g>
    </svg>

    <div class="brand"><span class="brand-dot"></span><span>Bluegate Lending Partners, Inc.</span></div>

    <h1 class="headline">100%<br>No Money<br>Down</h1>

    <section class="contact">
      <h2 class="gold-head">Contact<br>Marcus Delwyn</h2>
      <ul class="contact-list sc">
        <li>- NMLS #58307</li>
        <li>- Bluegate Lending Partners, Inc.</li>
        <li class="indent">4820 Harbor Crest Drive, Suite</li>
        <li class="indent">210B, Bowie, MD 20715</li>
        <li>- NMLS #916482</li>
      </ul>
      <h3 class="gold-head label">Email</h3>
      <p class="value">MDELWYN@BLUEGATELENDPRO.COM</p>
      <h3 class="gold-head label">Website</h3>
      <p class="value">WWW.BLUEGATELENDPRO.COM</p>
      <div class="phones">
        <svg width="28" height="44" viewBox="0 0 28 44" aria-hidden="true">
          <rect x="2" y="2" width="24" height="40" rx="4" fill="none" stroke="var(--gold)" stroke-width="3"/>
          <line x1="6" y1="8" x2="22" y2="8" stroke="var(--gold)" stroke-width="2"/>
          <line x1="6" y1="34" x2="22" y2="34" stroke="var(--gold)" stroke-width="2"/>
          <circle cx="14" cy="38.5" r="1.8" fill="var(--gold)"/>
        </svg>
        <div class="lines">(800) 555-0147 x17<br>(240) 555-0193 &nbsp;&nbsp;&nbsp;( Direct )</div>
      </div>
    </section>

    <section class="offer">
      <h2 class="gold-head">100% Investor Financing<br>Fix &amp; Flip Joint Ventures</h2>
      <ul class="perks sc">
        <li>Actually Get Money Back At Close</li>
        <li>Closing Costs Financed</li>
        <li>2-3 Week Close</li>
        <li>No Score Minimum</li>
        <li>No Reserve Requirement</li>
      </ul>
      <ul class="terms">
        <li class="sc">Depending on Experience</li>
        <li class="sc">Rates 10 - 12%</li>
        <li class="sc">Points 2 - 4%</li>
        <li class="sc">Profit Sharing 35 - 50%</li>
      </ul>
    </section>
  </div>
</div>
</body>
</html>
```